High End Business Card Design for Flooring Store

Looking for a new card design for our hardwood flooring company. We have no print budget for these and are open to cards made from wood, metal, cardstock with embossed print ... or any combination of these. No plastic.

We sell luxury products and I want the cards to reflect our image of quality and class.

Our contact information as such;
Employee Name
418 Colbrook Blvd.
Ashgrove, NS
K9R-3M5
(555) 214-3968
Employee email @velkaflooring.com

Target Market(s)

Home Builders

Contact Information for Business Card

Emnployee name, business contact information

```html
<!DOCTYPE html>
<html lang="en">
<head>
<meta charset="utf-8">
<title>Velka Flooring & Stairs – Business Card</title>
<link rel="stylesheet" href="https://fonts.googleapis.com/css2?family=Montserrat:wght@400;500&family=Arimo:wght@400&display=swap">
<style>
  :root {
    --backdrop: #4a4a4a;
    --card-dark: #1f1f1f;
    --silver-light: #f2f3f5;
    --silver-mid: #b9bbbf;
    --silver-dark: #6f7176;
    --ink: #1a1a1a;
    --brand-red: #a8262b;
    --accent-gold: #f2b316;
    --rule-gold: #9a7a1e;
    --tagline-grey: #5b5b5b;
    --text-light: #f2f2f2;
  }
  * { margin: 0; padding: 0; box-sizing: border-box; }
  html, body { width: 1200px; height: 675px; overflow: hidden; }
  body {
    background: var(--backdrop);
    font-family: "Arimo", Arial, sans-serif;
    position: relative;
  }
  .card {
    position: absolute;
    top: 200px;
    width: 490px;
    height: 280px;
    border-radius: 26px;
    overflow: hidden;
    box-shadow: 0 10px 24px rgba(0,0,0,0.35);
  }
  .card--front {
    left: 90px;
    background: linear-gradient(100deg,
      var(--silver-dark) 0%, var(--silver-mid) 22%, var(--silver-light) 40%,
      var(--silver-mid) 55%, var(--silver-dark) 70%, var(--silver-light) 86%, var(--silver-mid) 100%);
  }
  .card--back { left: 620px; background: var(--card-dark); }

  .brand { position: absolute; display: flex; flex-direction: column; align-items: center; gap: 4px; }
  .brand__row { display: flex; align-items: flex-end; gap: 10px; }
  .brand__square { width: 34px; height: 34px; margin-bottom: 8px; }
  .brand__name {
    font-family: "Montserrat", sans-serif;
    font-weight: 400;
    font-size: 60px;
    line-height: 1;
  }
  .brand__tagline {
    font-family: "Montserrat", sans-serif;
    font-weight: 500;
    font-size: 13px;
    line-height: 1.15;
    color: var(--tagline-grey);
    text-align: center;
  }
  .card--front .brand { left: 118px; top: 92px; }
  .card--front .brand__square { background: var(--ink); }
  .card--front .brand__name { color: var(--ink); }

  .card--back .brand { left: 30px; top: 40px; }
  .card--back .brand__square { background: var(--accent-gold); }
  .card--back .brand__name { color: var(--brand-red); font-size: 54px; }

  .holder {
    position: absolute;
    right: 232px;
    top: 186px;
    text-align: right;
  }
  .holder__role { color: var(--text-light); font-size: 13px; margin-bottom: 4px; }
  .holder__name { color: var(--brand-red); font-size: 14px; letter-spacing: 0.5px; text-transform: uppercase; }

  .divider {
    position: absolute;
    left: 270px;
    top: 150px;
    width: 1px;
    height: 80px;
    background: var(--rule-gold);
  }
  .contact { position: absolute; left: 282px; top: 150px; list-style: none; }
  .contact__item {
    display: flex;
    align-items: flex-start;
    gap: 6px;
    color: var(--text-light);
    font-size: 12.5px;
    line-height: 1.3;
    margin-bottom: 4px;
  }
  .contact__icon { width: 12px; height: 12px; flex: none; margin-top: 2px; fill: var(--brand-red); }
</style>
</head>
<body>

  <section class="card card--front" aria-label="Card front">
    <div class="brand">
      <div class="brand__row">
        <span class="brand__square"></span>
        <span class="brand__name">Velka</span>
      </div>
      <p class="brand__tagline">Planchers &amp; Escaliers<br>Flooring &amp; Stairs</p>
    </div>
  </section>

  <section class="card card--back" aria-label="Card back">
    <div class="brand">
      <div class="brand__row">
        <span class="brand__square"></span>
        <span class="brand__name">Velka</span>
      </div>
      <p class="brand__tagline">Planchers &amp; Escaliers<br>Flooring &amp; Stairs</p>
    </div>

    <div class="holder">
      <p class="holder__role">Manager</p>
      <p class="holder__name">Alden Marsh</p>
    </div>

    <span class="divider"></span>

    <ul class="contact">
      <li class="contact__item">
        <svg class="contact__icon" viewBox="0 0 24 24"><path d="M6.6 10.8a15 15 0 0 0 6.6 6.6l2.2-2.2c.3-.3.7-.4 1-.2 1.1.4 2.3.6 3.6.6.6 0 1 .4 1 1V20c0 .6-.4 1-1 1A17 17 0 0 1 3 4c0-.6.4-1 1-1h3.5c.6 0 1 .4 1 1 0 1.3.2 2.5.6 3.6.1.3 0 .7-.2 1z"/></svg>
        <span>(555) 214-3968</span>
      </li>
      <li class="contact__item">
        <svg class="contact__icon" viewBox="0 0 24 24"><path d="M2 5h20v14H2zm2 2v.5l8 5 8-5V7l-8 5z"/></svg>
        <span>alden@velkaflooring.com</span>
      </li>
      <li class="contact__item">
        <svg class="contact__icon" viewBox="0 0 24 24"><path d="M12 2a7 7 0 0 0-7 7c0 5 7 13 7 13s7-8 7-13a7 7 0 0 0-7-7zm0 9.5A2.5 2.5 0 1 1 12 6.5a2.5 2.5 0 0 1 0 5z"/></svg>
        <span>418 Colbrook Blvd.<br>Ashgrove, NS, K9R-3M5</span>
      </li>
    </ul>
  </section>

</body>
</html>
```